Slick Quillnest Ad

We've recently re-branded our business to reflect our ethos "Wealth is about more than money - it's about choice." We aim to protect your hard-earned success and help achieve your lifestyle aspirations, whether that's retiring at fifty to go globetrotting, or buying your first home. We're a financial consultancy that primarily services high-net-worth clients.

Our brand is minimalist, modern (check out our website) and the brief focuses on our strong investment return for the past 12 years.

Task: The attached brief is for a Quillnest advertisement. Please see competitor images as a guide to how 'returns' and 'branding' can both be displayed in a design.

Target Market(s)

+30

Font styles to use
Sans Serif

Requirements
Must have
• Creative should feature the strong investment return, and design aesthetic should be 'on-brand' (modern, minimalist, lifestyle focused).

```html
<!DOCTYPE html>
<html lang="en">
<head>
<meta charset="utf-8">
<title>Quillnest – Global Investment Returns</title>
<link rel="stylesheet" href="https://fonts.googleapis.com/css2?family=Montserrat:wght@300;400;700;800&display=swap">
<style>
  :root {
    --paper: #ffffff;
    --ink: #3b3b3b;
    --brand-green: #a3b33a;
    --night: #141210;
    --dusk: #2b2119;
    --ember: #8a5a2c;
    --glow: #d49a52;
    --logo-light: #ffffff;
  }
  * { box-sizing: border-box; margin: 0; padding: 0; }
  html, body {
    width: 1200px;
    height: 640px;
    overflow: hidden;
    background: var(--night);
  }
  .ad {
    position: relative;
    width: 1200px;
    height: 640px;
    overflow: hidden;
    font-family: "Montserrat", Arial, sans-serif;
  }
  .ad__photo {
    position: absolute;
    inset: 0;
    background:
      radial-gradient(ellipse 260px 120px at 1020px 390px, var(--glow) 0%, rgba(212,154,82,0.45) 35%, rgba(212,154,82,0) 100%),
      radial-gradient(ellipse 620px 260px at 980px 380px, rgba(138,90,44,0.75) 0%, rgba(138,90,44,0) 100%),
      linear-gradient(180deg, #1c1915 0%, var(--dusk) 45%, #3a2a1c 62%, #221a13 78%, var(--night) 100%);
  }
  .ad__panel {
    position: absolute;
    inset: 0;
    width: 1200px;
    height: 640px;
  }
  .brand-mark {
    position: absolute;
    left: 30px;
    top: 82px;
    display: flex;
    align-items: center;
    gap: 12px;
    color: var(--brand-green);
    font-weight: 700;
    font-size: 30px;
  }
  .brand-mark__dot {
    width: 22px;
    height: 22px;
    border-radius: 50%;
    background: var(--brand-green);
  }
  .headline {
    position: absolute;
    left: 28px;
    top: 212px;
    color: var(--ink);
    font-weight: 300;
    font-size: 45px;
    line-height: 54px;
    letter-spacing: -0.5px;
  }
  .headline__lead { display: block; }
  .headline__figure {
    color: var(--brand-green);
    font-weight: 800;
    font-size: 40px;
    line-height: 50px;
    letter-spacing: 0;
  }
  .headline__period {
    display: block;
    font-weight: 700;
    font-size: 54px;
    line-height: 64px;
    letter-spacing: 0;
  }
  .signoff {
    position: absolute;
    left: 918px;
    top: 538px;
    display: flex;
    align-items: center;
    gap: 10px;
    color: var(--logo-light);
    font-weight: 700;
    font-size: 28px;
  }
  .signoff__dot {
    width: 20px;
    height: 20px;
    border-radius: 50%;
    background: var(--logo-light);
  }
</style>
</head>
<body>
  <main class="ad">
    <div class="ad__photo" role="img" aria-label="Lifestyle photo: a family silhouetted holding hands, walking along a beach at sunset"></div>

    <svg class="ad__panel" viewBox="0 0 1200 640" aria-hidden="true">
      <path d="M0 0 H488 Q782 320 516 640 H0 Z" fill="var(--paper)"/>
    </svg>

    <div class="brand-mark">
      <span class="brand-mark__dot"></span>
      <span>Quillnest</span>
    </div>

    <h1 class="headline">
      <span class="headline__lead">Our global</span>
      <span class="headline__lead">investment portfolio</span>
      <span class="headline__lead"><strong class="headline__figure">Delivered 20.5%</strong></span>
      <span class="headline__lead"><strong class="headline__figure">returns</strong> over the past</span>
      <span class="headline__period">12 months</span>
    </h1>

    <div class="signoff">
      <span class="signoff__dot"></span>
      <span>Quillnest</span>
    </div>
  </main>
</body>
</html>
```